I need creative and unique business card design using my company logo. Ok to change logo color. We are a small brokerage doing both Real Estate and Mortgage services. Need to have the follow on business card;
1. agent name - Mila Fenton - Realtor
2. cell - 949-555-0182
3. license number - DRE 04917362
4. business name - Brightway Estates & Lending, Inc
5. business office - 626-555-0147
6. business address - 287 W. Larkmoor Ave #214, Arcadia CA 91088
7. business logo - attached (ok to use different color on logo)

```html
<!DOCTYPE html>
<html lang="en">
<head>
<meta charset="utf-8">
<title>Brightway Estates &amp; Lending — Business Card</title>
<link rel="stylesheet" href="https://fonts.googleapis.com/css2?family=Montserrat:wght@500;700&family=Mulish:wght@400&display=swap">
<style>
  :root {
    --stage: #8c7357;
    --card: #ffffff;
    --navy: #234f9c;
    --sky: #3f8fd6;
    --ink: #1d1d1d;
    --rule: #27478a;
    --back-light: #6a9fdc;
    --back-mid: #3a72c0;
    --back-deep: #1f56a6;
  }
  * { box-sizing: border-box; margin: 0; padding: 0; }
  html, body { width: 900px; height: 1200px; overflow: hidden; }
  body { background: var(--stage); position: relative; font-family: "Mulish", sans-serif; }

  .card {
    position: absolute;
    left: 68px;
    width: 758px;
    height: 440px;
    border-radius: 38px;
    overflow: hidden;
  }
  .card--front { top: 133px; background: var(--card); }
  .card--back {
    top: 638px;
    background: linear-gradient(135deg, var(--back-light) 0%, var(--back-mid) 45%, var(--back-deep) 100%);
  }

  .brand {
    position: absolute;
    right: 40px;
    top: 32px;
    width: 300px;
    text-align: center;
  }
  .brand__mark {
    display: block;
    width: 122px;
    height: 122px;
    margin: 0 0 0 108px;
    background: var(--navy);
  }
  .brand__name {
    margin-top: 20px;
    font-family: "Montserrat", sans-serif;
    font-weight: 500;
    font-size: 17px;
    letter-spacing: 2px;
    line-height: 1.3;
    color: var(--navy);
    text-transform: uppercase;
  }

  .agent { position: absolute; left: 33px; top: 222px; }
  .agent__name {
    font-family: "Montserrat", sans-serif;
    font-weight: 700;
    font-size: 23px;
    color: var(--navy);
  }
  .agent__name .surname { color: var(--sky); }
  .agent__title { margin-top: 4px; font-size: 16px; color: var(--ink); }

  .rule {
    position: absolute;
    left: 33px;
    top: 279px;
    width: 685px;
    height: 1.5px;
    background: var(--rule);
  }

  .address {
    position: absolute;
    left: 33px;
    top: 303px;
    font-size: 16.5px;
    line-height: 20px;
    color: var(--ink);
    font-style: normal;
  }

  .phones { position: absolute; left: 33px; top: 356px; list-style: none; }
  .phones li {
    display: flex;
    align-items: center;
    height: 26px;
    font-size: 16.5px;
    color: var(--ink);
  }
  .phones svg { width: 16px; height: 18px; margin-right: 14px; fill: var(--navy); }

  .license {
    position: absolute;
    right: 45px;
    top: 381px;
    font-size: 16px;
    color: var(--ink);
  }
</style>
</head>
<body>

<section class="card card--front" aria-label="Business card front">
  <div class="brand">
    <span class="brand__mark" aria-hidden="true"></span>
    <p class="brand__name">Brightway Estates<br>&amp; Lending, Inc</p>
  </div>

  <div class="agent">
    <h1 class="agent__name">Mila <span class="surname">Fenton</span></h1>
    <p class="agent__title">Realtor</p>
  </div>

  <div class="rule"></div>

  <address class="address">287 W. Larkmoor Ave #214,<br>Arcadia CA 91088</address>

  <ul class="phones">
    <li>
      <svg viewBox="0 0 16 18" aria-label="Office phone"><path d="M1 7c0-3 3-4 7-4s7 1 7 4l-1 1.5h-3L10 6H6L5 8.5H2zM4 9h8l2 6H2z"/></svg>
      626-555-0147
    </li>
    <li>
      <svg viewBox="0 0 16 18" aria-label="Mobile phone"><path d="M4 0h8a1.5 1.5 0 0 1 1.5 1.5v15A1.5 1.5 0 0 1 12 18H4a1.5 1.5 0 0 1-1.5-1.5v-15A1.5 1.5 0 0 1 4 0zm0 2v12h8V2zm4 13a1 1 0 1 0 0 2 1 1 0 0 0 0-2z"/></svg>
      949-555-0182
    </li>
  </ul>

  <p class="license">License number - DRE 04917362</p>
</section>

<section class="card card--back" role="img" aria-label="Card back: repeating brand mark pattern in blue tones"></section>

</body>
</html>
```